Poster for a Bicycle show/Expo

We need a poster for a Bicycle show/Expo and sustainable transport. Exhibitors will sell bikes, cycling clothing, accessories, etc. ...
This show is annual and the Poster is for the 2016 edition.

Your concept must be compatible in a landscape format. (We will ourselves adaptations of different formats.)
Width: 210 mm
Height: 297 mm
It's necessary for us to have the source file (vector) for make, later, the different format (flyers, website, ...)

Content of the Poster:
- 1 big picture (one of the two attached)
- Big title (typo-title worked): « Foire du Rouet » (« Salon » or « Salon du » can be small and « Vélo » big.)
- Subtitle: « et de la mobilité durable »
- Date: « 18, 19 et 20 mars 2016 » or « 18-20 mars 2016 »
- Place: « Halle RTP - Gare de Plantaz »
- Text line 1: « www.foire-du-rouet.ch »
- Text line 2: « Entrée gratuite »
- Text line 3: « Ve 18 mars de 17h à 20h - Sa 19 mars de 10h à 18h - Di 20 mars de 10h à 17h »
- Please, leave a zone in the poster for sponsors logos
(The predominant information (most visible) are: « Vélo » and « 18, 19 et 20 mars 2016 » or « 18-20 mars 2016 »)

Target Market(s)

Bicycle fan

Industry/Entity Type

Sporting Good

Font styles to use
Serif
Sans Serif

Colors
add136
ffffff
ec1f27

Requirements
Must have
• The style must be modern, dynamic, bright colors.

```html
<!DOCTYPE html>
<html lang="fr">
<head>
<meta charset="utf-8">
<title>Foire du Rouet 2016</title>
<link rel="stylesheet" href="https://fonts.googleapis.com/css2?family=Source+Sans+3:wght@400;600;700;900&display=swap">
<style>
  :root {
    --red: #ec1f27;
    --green: #add136;
    --white: #ffffff;
    --navy: #1c2f5a;
    --sky-top: #2a74c4;
    --sky-mid: #5d9fe0;
    --sky-low: #a9d0f2;
    --grey: #b9b9b9;
  }
  * { margin: 0; padding: 0; box-sizing: border-box; }
  html, body { width: 849px; height: 1200px; overflow: hidden; background: var(--white); }
  body { font-family: "Source Sans 3", Arial, sans-serif; }
  .poster { position: relative; width: 849px; height: 1200px; overflow: hidden; background: var(--white); }

  .sky-photo {
    position: absolute; left: 0; top: 0; width: 849px; height: 1000px;
    background:
      radial-gradient(ellipse 180px 60px at 140px 330px, rgba(255,255,255,.85), transparent 70%),
      radial-gradient(ellipse 220px 70px at 720px 780px, rgba(255,255,255,.8), transparent 70%),
      radial-gradient(ellipse 260px 150px at 320px 180px, rgba(255,255,255,.55), transparent 70%),
      radial-gradient(ellipse 160px 50px at 120px 560px, rgba(255,255,255,.7), transparent 70%),
      linear-gradient(180deg, var(--sky-top) 0%, var(--sky-mid) 45%, var(--sky-low) 100%);
  }

  .title { position: absolute; left: 0; top: 0; width: 849px; font-weight: inherit; }
  .title-small, .title-big {
    position: absolute; left: 0; width: 849px; padding-left: 110px;
    text-align: center; color: var(--red); line-height: 1;
    paint-order: stroke fill;
  }
  .title-small {
    top: 336px; font-size: 92px; font-weight: 700; letter-spacing: -1px;
    -webkit-text-stroke: 5px var(--white);
  }
  .title-big {
    top: 428px; font-size: 196px; font-weight: 900; letter-spacing: -6px;
    -webkit-text-stroke: 6px var(--white);
  }
  .subtitle {
    position: absolute; left: 0; width: 849px; top: 648px; padding-left: 338px;
    font-size: 33px; font-weight: 600; color: var(--navy); line-height: 1;
  }
  .date {
    position: absolute; left: 0; width: 849px; top: 698px; text-align: center;
    font-size: 70px; font-weight: 700; color: var(--red); letter-spacing: -1px; line-height: 1;
    -webkit-text-stroke: 4px var(--white); paint-order: stroke fill;
  }
  .venue {
    position: absolute; left: 0; width: 849px; top: 776px; text-align: center;
    font-size: 44px; font-weight: 700; color: var(--navy); line-height: 1;
  }
  .info-box {
    position: absolute; top: 836px; height: 86px; border-radius: 10px;
    color: var(--white); font-weight: 700;
  }
  .info-box--access {
    left: 42px; width: 358px; background: var(--green);
    padding: 12px 20px; font-size: 27px; line-height: 31px;
  }
  .info-box--hours {
    left: 428px; width: 368px; background: var(--red);
    padding: 6px 18px; font-size: 21px; line-height: 25px; font-weight: 600;
  }
  .swoosh { position: absolute; left: 0; top: 920px; width: 849px; height: 120px; }
  .sponsor-zone {
    position: absolute; left: 0; width: 849px; top: 1110px; text-align: center;
    font-size: 30px; font-weight: 400; color: var(--grey);
  }
</style>
</head>
<body>
<main class="poster">
  <div class="sky-photo" role="img" aria-label="Ciel bleu avec nuages, un nuage en forme de vélo au-dessus du titre"></div>

  <h1 class="title">
    <span class="title-small">Foire du</span>
    <span class="title-big">Rouet</span>
  </h1>
  <p class="subtitle">et de la mobilité durable</p>
  <p class="date">18, 19 et 20 mars 2016</p>
  <p class="venue">Halle RTP - Gare de Plantaz</p>

  <div class="info-box info-box--access">
    www.foire-du-rouet.ch<br>Entrée gratuite
  </div>
  <div class="info-box info-box--hours">
    Ve 18 mars de 17h à 20h - Sa<br>19 mars de 10h à 18h - Di 20<br>mars de 10h à 17h
  </div>

  <svg class="swoosh" viewBox="0 0 849 120" aria-hidden="true">
    <path d="M0 30 C 250 110, 600 110, 849 20 L849 120 L0 120 Z" fill="var(--green)"/>
    <path d="M0 52 C 250 128, 600 128, 849 42 L849 120 L0 120 Z" fill="var(--red)"/>
    <path d="M0 62 C 250 136, 600 136, 849 54 L849 120 L0 120 Z" fill="var(--white)"/>
  </svg>

  <p class="sponsor-zone">for sponsor</p>
</main>
</body>
</html>
```